KTW Ledgerwise Office Services Pty Ltd

Design a website for bookkeeping & accounting company

I like this website as an example with my own branding

https://go.quillcount.example/sydney-bookkeeping-lp/?keyword=bookkeeping%20sydney&matchtype=e&campaignid=482913057&device=c&adgroupid=31852064917&adposition=1t1&creative=607314928150&gclid=XkPwQrTbLmN3vZ8yHs5cDf2GaJ_uE0oWnRiYtBpKqLzMvXs_TeC

Number of Pages Required

1 page

Font styles to use
Sans Serif

Colors
9bcb3c

```html
<!DOCTYPE html>
<html lang="en">
<head>
<meta charset="utf-8">
<title>KTW Ledgerwise Office Services Pty Ltd</title>
<link rel="stylesheet" href="https://fonts.googleapis.com/css2?family=Open+Sans:wght@400;600;700&display=swap">
<style>
:root{
  --green:#8cc530;
  --ink:#1c1c1c;
  --text:#444;
  --panel:#efefef;
  --footer:#2f2f2f;
  --white:#fff;
}
*{box-sizing:border-box;margin:0;padding:0}
html,body{width:1200px;height:2387px;overflow:hidden;background:var(--white)}
body{position:relative;font-family:"Open Sans",Arial,sans-serif;color:var(--ink)}
.abs{position:absolute}

/* header */
.site-header{left:0;top:0;width:1200px;height:88px;background:var(--white)}
.brand{left:132px;top:30px;display:flex;align-items:center;gap:10px}
.brand-mark{width:26px;height:26px;background:var(--green)}
.brand-name{font-size:15px;font-weight:700;color:var(--ink);line-height:1.2;width:220px}
.main-nav{right:134px;top:38px;display:flex;gap:38px;font-size:13.5px}
.main-nav a{color:var(--ink);text-decoration:none}
.main-nav a.active{color:var(--green)}

/* hero */
.hero{left:0;top:88px;width:1200px;height:702px;overflow:hidden}
.hero-photo{position:absolute;inset:0;background:
  radial-gradient(ellipse at 62% 38%,#c9ced3 0%,#8b8f93 28%,#4a4642 55%,#2a2624 100%)}
.hero-curve{position:absolute;left:0;top:0}
.hero-title{left:132px;top:190px;color:var(--white);font-size:32px;font-weight:700;line-height:1.25}
.btn{left:134px;top:286px;width:130px;height:40px;background:var(--green);color:var(--white);
  font-size:15px;font-weight:700;display:flex;align-items:center;justify-content:center;letter-spacing:.3px}
.hero-arrow{top:232px}

/* intro */
.intro-photo{left:135px;top:730px;width:424px;height:424px;border-radius:50%;border:13px solid #d8d8d8;
  background:linear-gradient(160deg,#5b5d60 0%,#b3b6b9 45%,#e8e9ea 75%,#9ea1a4 100%)}
.intro-title{left:600px;top:735px;width:480px;font-size:25px;font-weight:700;line-height:1.4}
.intro-text{left:600px;top:812px;width:466px;font-size:12px;line-height:21.5px;color:var(--text)}
.service{left:600px;width:466px;height:126px;background:var(--panel)}
.service svg{position:absolute;left:33px;top:28px}
.service h3{position:absolute;left:126px;top:14px;font-size:20px;font-weight:700}
.service p{position:absolute;left:126px;top:50px;width:320px;font-size:12px;line-height:19.5px;color:var(--text)}

/* testimonials */
.testimonials{left:0;top:1442px;width:1200px;height:412px;background:var(--green)}
.testi-title{left:134px;top:48px;font-size:25px;font-weight:700}
.testi-intro{left:134px;top:88px;width:240px;font-size:12px;line-height:19px;color:var(--ink)}
.testi-nav{left:134px;top:180px;display:flex;gap:10px}
.testi-nav span{width:21px;height:21px;border:1.5px solid var(--ink);display:flex;align-items:center;justify-content:center}
.card{top:56px;width:206px;height:300px;background:var(--white);text-align:center}
.avatar{position:absolute;left:54px;top:22px;width:98px;height:98px;border-radius:50%;
  background:linear-gradient(180deg,#9a9a9a,#3f3f3f)}
.quote{position:absolute;left:16px;top:138px;width:174px;font-size:13.5px;line-height:23px;color:var(--text)}
.card-name{position:absolute;left:0;top:260px;width:100%;font-size:14.5px;font-weight:700}

/* contact */
.contact-title{left:0;top:1922px;width:1200px;text-align:center;font-size:24px;font-weight:700}
.map{left:132px;top:1967px;width:468px;height:237px;
  background:linear-gradient(135deg,#e4e6e4 0%,#d6dbd2 40%,#cfe0b8 60%,#e2e4e2 100%)}
.contact-panel{left:600px;top:1967px;width:466px;height:237px;background:var(--panel)}
.contact-line{position:absolute;left:34px;font-size:16px;color:var(--ink)}
.social{position:absolute;top:156px;width:42px;height:42px;border-radius:50%;background:#6d6d6d}

/* footer */
.site-footer{left:0;top:2287px;width:1200px;height:100px;background:var(--footer);color:#c9c9c9;text-align:center}
.footer-nav{position:absolute;top:27px;width:100%;font-size:12px}
.footer-nav span{margin:0 8px}
.copyright{position:absolute;top:54px;width:100%;font-size:12px}
</style>
</head>
<body>

<header class="site-header abs">
  <div class="brand abs">
    <span class="brand-mark"></span>
    <span class="brand-name">KTW Ledgerwise Office Services Pty Ltd</span>
  </div>
  <nav class="main-nav abs">
    <a class="active" href="#">Home</a><a href="#">Services</a><a href="#">About Us</a><a href="#">Testimonials</a><a href="#">Contact Us</a>
  </nav>
</header>

<section class="hero abs">
  <div class="hero-photo" role="img" aria-label="Photo of a hand using a tablet showing charts"></div>
  <svg class="hero-curve" width="1200" height="702" viewBox="0 0 1200 702">
    <path d="M0 697 C 300 560, 640 490, 1200 524 L1200 702 L0 702 Z" fill="#8cc530"/>
    <path d="M0 702 C 320 568, 660 500, 1200 540 L1200 702 Z" fill="#fff"/>
  </svg>
  <h1 class="hero-title abs">Pellentesque blandit<br>lacus eget nunc faucibus</h1>
  <div class="btn abs">CONTACT US</div>
  <svg class="hero-arrow abs" style="left:48px" width="20" height="34" viewBox="0 0 20 34"><path d="M17 3 L4 17 L17 31" fill="none" stroke="#fff" stroke-width="4"/></svg>
  <svg class="hero-arrow abs" style="left:1132px" width="20" height="34" viewBox="0 0 20 34"><path d="M3 3 L16 17 L3 31" fill="none" stroke="#fff" stroke-width="4"/></svg>
</section>

<div class="intro-photo abs" role="img" aria-label="Photo of a businessman signing a document"></div>
<h2 class="intro-title abs">Fusce nec leo ac urna pulvinar auctor. Mauris bibendum fringilla velit.</h2>
<p class="intro-text abs">Aliquam erat volutpat. Etiam quis aliquet risus. Duis ornare erat eget magna dapibus, in accumsan quam pharetra. Nam tempus, quam in bibendum vulputate, sapien dolor viverra nisl, vitae euismod elit turpis et nulla. Aliquam erat volutpat. Pellentesque blandit lacus eget nunc faucibus, et tincidunt eros viverra. Phasellus consequat sagittis nisi suscipit feugiat. Cras eget leo sed nunc hendrerit ultricies eu at nisi.</p>

<article class="service abs" style="top:945px">
  <svg width="64" height="70" viewBox="0 0 64 70" fill="none" stroke="#222" stroke-width="2.5">
    <rect x="4" y="2" width="56" height="66" rx="6"/><rect x="12" y="10" width="40" height="14"/>
    <rect x="12" y="32" width="8" height="7"/><rect x="28" y="32" width="8" height="7"/><rect x="44" y="32" width="8" height="7"/>
    <rect x="12" y="45" width="8" height="7"/><rect x="28" y="45" width="8" height="7"/><rect x="44" y="45" width="8" height="16"/>
    <rect x="12" y="56" width="24" height="5"/>
  </svg>
  <h3>Praesent iaculis faucibus</h3>
  <p>Maecenas consequat justo enim, ac mattis massa imperdiet quis. Fusce eget neque elit. Sed augue orci, elementum in magna congue, tincidunt vulputate.</p>
</article>
<article class="service abs" style="top:1089px">
  <svg width="64" height="72" viewBox="0 0 64 72" fill="none" stroke="#222" stroke-width="2.5">
    <path d="M8 8 L46 4 L52 62 L14 68 Z"/><rect x="4" y="12" width="40" height="56"/>
    <circle cx="26" cy="32" r="10"/><path d="M26 22 V32 H36"/>
    <path d="M10 50 H36 M10 56 H30 M10 62 H36"/>
  </svg>
  <h3>Vestibulum condimentum</h3>
  <p>Maecenas consequat justo enim, ac mattis massa imperdiet quis. Fusce eget neque elit. Sed augue orci, elementum in magna congue, tincidunt vulputate.</p>
</article>
<article class="service abs" style="top:1233px">
  <svg width="70" height="72" viewBox="0 0 70 72" fill="none" stroke="#222" stroke-width="2.5">
    <circle cx="26" cy="30" r="18"/><circle cx="26" cy="30" r="12"/>
    <path d="M39 43 L60 64" stroke-width="6"/><path d="M18 34 L24 26 L30 32 L36 24"/>
    <path d="M48 14 L62 2 M56 2 H62 V8"/>
  </svg>
  <h3>Etiam mattis augue</h3>
  <p>Maecenas consequat justo enim, ac mattis massa imperdiet quis. Fusce eget neque elit. Sed augue orci, elementum in magna congue, tincidunt vulputate.</p>
</article>

<section class="testimonials abs">
  <h2 class="testi-title abs">Testimonials</h2>
  <p class="testi-intro abs">Maecenas consequat justo enim, ac mattis massa imperdiet quis. Fusce eget neque elit. Sed augue orci, elementum in magna congue, tincidunt vulputate.</p>
  <div class="testi-nav abs">
    <span><svg width="8" height="12" viewBox="0 0 8 12"><path d="M6 1 L1 6 L6 11" fill="none" stroke="#1c1c1c" stroke-width="1.5"/></svg></span>
    <span><svg width="8" height="12" viewBox="0 0 8 12"><path d="M2 1 L7 6 L2 11" fill="none" stroke="#1c1c1c" stroke-width="1.5"/></svg></span>
  </div>
  <div class="card abs" style="left:406px">
    <div class="avatar" role="img" aria-label="Portrait of client Peter Hale"></div>
    <p class="quote">“ Fusce vitae lectus sit amet mi pulvinar maximus. Aenean placerat, nibh vel accumsan aliquet magna nibh accumsan nibh. ”</p>
    <div class="card-name">Peter Hale</div>
  </div>
  <div class="card abs" style="left:633px">
    <div class="avatar" role="img" aria-label="Portrait of client Nora"></div>
    <p class="quote">“ Fusce vitae lectus sit amet mi pulvinar maximus. Aenean placerat, nibh vel accumsan aliquet magna nibh accumsan nibh. ”</p>
    <div class="card-name">Nora</div>
  </div>
  <div class="card abs" style="left:861px">
    <div class="avatar" role="img" aria-label="Portrait of client Tobias"></div>
    <p class="quote">“ Fusce vitae lectus sit amet mi pulvinar maximus. Aenean placerat, nibh vel accumsan aliquet magna nibh accumsan nibh. ”</p>
    <div class="card-name">Tobias</div>
  </div>
</section>

<h2 class="contact-title abs">Contact Us</h2>
<div class="map abs" role="img" aria-label="Street map of the office location"></div>
<div class="contact-panel abs">
  <p class="contact-line" style="top:37px">24 Building name, Street name, City Zipcode</p>
  <p class="contact-line" style="top:74px">Phone : 555 014 2290</p>
  <p class="contact-line" style="top:110px">Email : info@ledgerwiseoffice.example</p>
  <span class="social" style="left:35px" aria-label="Social link"></span>
  <span class="social" style="left:97px" aria-label="Social link"></span>
  <span class="social" style="left:157px" aria-label="Social link"></span>
</div>

<footer class="site-footer abs">
  <div class="footer-nav">Home<span>|</span>Services<span>|</span>About Us<span>|</span>Testimonials<span>|</span>Contact Us</div>
  <div class="copyright">Copyright © 2018 Ledgerwise Office Services. &nbsp;All rights reserved.</div>
</footer>

</body>
</html>
```